Business card design only (Have Logo Online) Shoudl be quick and easy for designer

We would like to have a business card design that is in-line with our company logo. Final deliverables should include two EPS extension file. One for the front card design and the other the back-end design. Please also indicate the font style used.

Advisory Pebbles is a social enterprise that focuses on utilizing technology, unique methodologies and international partnerships to provide a one-stop location for economical and dependable IT-related solutions.

Target Market(s)

Micro, small and medium business owners.

Industry/Entity Type

Business

Requirements
Must have
• The business card should incorporate our company logo.
Nice to have
• A little web 2.0 style would be nice but I haven''t decided yet.

```html
<!DOCTYPE html>
<html lang="en">
<head>
<meta charset="utf-8">
<title>Advisory Pebbles – Business Card</title>
<link href="https://fonts.googleapis.com/css2?family=Roboto+Condensed:wght@400;500;700&family=Montserrat:wght@500;600;700&display=swap" rel="stylesheet">
<style>
  :root {
    --ink: #111111;
    --paper: #ffffff;
    --green-deep: #52925a;
    --green-brand: #3f8a4e;
    --green-soft: #bfdf9c;
    --green-pale: #d3e6d6;
    --green-text: #c4e3a2;
  }
  * { margin: 0; padding: 0; box-sizing: border-box; }
  html, body { width: 1200px; height: 686px; overflow: hidden; background: var(--paper); }
  body { position: relative; font-family: "Roboto Condensed", "Arial Narrow", sans-serif; color: var(--ink); }

  .card { position: absolute; top: 23px; width: 365px; height: 639px; border: 2px solid var(--ink); overflow: hidden; }
  .card--front { left: 194px; background: var(--paper); }
  .card--back { left: 629px; background: var(--green-soft); }

  /* front */
  .brand-disc { position: absolute; left: 14px; top: 28px; width: 150px; height: 150px; border-radius: 50%; background: var(--green-soft); opacity: .85; }
  .brand-name { position: absolute; left: 48px; top: 128px; font-weight: 700; font-size: 27px; letter-spacing: 1px; color: var(--green-brand); white-space: nowrap; }

  .decor-disc { position: absolute; left: 135px; top: 305px; width: 250px; height: 250px; border-radius: 50%; background: var(--green-pale); opacity: .7; }

  .name-row { position: absolute; left: 0; right: 0; top: 232px; display: flex; align-items: baseline; }
  .name-rule { width: 29px; height: 3px; background: var(--ink); margin-right: 6px; align-self: center; }
  .person-name { font-size: 32px; font-weight: 400; white-space: nowrap; margin-right: 8px; }
  .person-role { font-family: "Montserrat", sans-serif; font-weight: 700; font-size: 16px; color: var(--green-deep); white-space: nowrap; margin-right: 4px; }
  .role-rule { flex: 1; height: 2px; background: var(--green-deep); align-self: center; margin-top: 10px; }

  .address { position: absolute; left: 35px; top: 293px; font-size: 18px; line-height: 25px; font-weight: 700; font-style: normal; }

  .contact-label { position: absolute; left: 22px; width: 74px; height: 23px; background: var(--green-deep); color: var(--paper); font-size: 15px; font-weight: 700; line-height: 23px; padding-left: 8px; border-radius: 22px 4px 22px 4px; }
  .contact-label--cell { top: 413px; }
  .contact-label--mail { top: 499px; }
  .contact-value { position: absolute; left: 35px; font-size: 17px; font-weight: 700; white-space: nowrap; }
  .contact-value--cell { top: 446px; }
  .contact-value--mail { top: 531px; font-size: 16px; }

  .web-rule { position: absolute; left: 0; right: 0; height: 2px; background: var(--green-deep); }
  .web-rule--top { top: 578px; }
  .web-rule--bottom { top: 627px; }
  .web-band { position: absolute; left: 0; right: 0; top: 588px; height: 35px; background: var(--green-soft); text-align: center; font-family: "Montserrat", sans-serif; font-weight: 600; font-size: 19px; line-height: 35px; color: var(--ink); }

  /* back */
  .back-rule { position: absolute; left: 0; right: 0; height: 2px; background: var(--green-deep); }
  .back-rule--top { top: 326px; }
  .back-rule--bottom { top: 573px; }
  .goal-panel { position: absolute; left: 0; right: 0; top: 333px; height: 236px; background: var(--green-deep); padding: 42px 0 0 23px; color: var(--green-text); }
  .goal-title { font-family: "Montserrat", sans-serif; font-weight: 500; font-size: 18px; letter-spacing: .5px; margin-bottom: 12px; white-space: nowrap; }
  .goal-text { font-size: 19px; line-height: 30.5px; font-weight: 500; }
  .goal-line { display: block; white-space: nowrap; transform: scaleX(.9); transform-origin: left; }
  .goal-panel strong { color: var(--paper); font-weight: 700; }
</style>
</head>
<body>
  <section class="card card--front" aria-label="Front of business card">
    <div class="brand-disc" aria-hidden="true"></div>
    <div class="brand-name">ADVISORY PEBBLES</div>
    <div class="decor-disc" aria-hidden="true"></div>

    <div class="name-row">
      <div class="name-rule"></div>
      <h1 class="person-name">Marlon Teague</h1>
      <div class="person-role">FOUNDER</div>
      <div class="role-rule"></div>
    </div>

    <address class="address">4120 Alder Lane<br>BC Canada<br>V6T 2K9</address>

    <div class="contact-label contact-label--cell">CELL:</div>
    <div class="contact-value contact-value--cell">1-604-555-0148</div>
    <div class="contact-label contact-label--mail">E-MAIL:</div>
    <div class="contact-value contact-value--mail">marlon.teague@advisorypebbles.com</div>

    <div class="web-rule web-rule--top"></div>
    <div class="web-band">www.advisorypebbles.com</div>
    <div class="web-rule web-rule--bottom"></div>
  </section>

  <section class="card card--back" aria-label="Back of business card">
    <div class="back-rule back-rule--top"></div>
    <div class="goal-panel">
      <p class="goal-title">OUR <strong>ULTIMATE GOAL</strong> IS...</p>
      <p class="goal-text">
        <span class="goal-line">...to provide a <strong>one-stop</strong> location for micro</span>
        <span class="goal-line">and small business owners to attend to</span>
        <span class="goal-line">all their business functions in an</span>
        <span class="goal-line"><strong>economical</strong> and <strong>time efficient</strong> way.</span>
      </p>
    </div>
    <div class="back-rule back-rule--bottom"></div>
  </section>
</body>
</html>
```